Moss&Lark

I'm writing a book and need a front and back cover for the book.

IMPORTANT DETAILS:
TITLE: Moss & Lark
SUBTITLE: Twelve empowering true stories of women who found strength and hope in times of darkness and despair.
AUTHORS: Marnie Tolliver & Dalia Pratt
1. The book is about WOMEN'S stories of struggle (MOSS) and overcoming them with a hopeful and inspiring story at the end (LARK). So the cover of the book should depict these opposing / conflicting ideas.

2. The cover needs to be clean and simple

3. a.The font for the word MOSS should look stronger/bolder/more intense/sturdier/a little more masculine....
b. The ampersand (&) between Moss & Lark should tie the two fonts together
c. The font for the word LARK should look fluid/clean/EASY-TO-READ cursive script

4. I'm open to different color fonts with a limit of 3 colors MAX

5. For the back cover: This will be a collection of stories from 12 total authors so the back cover needs to have room for 12 faces somehow.

Looking forward to it.

```html
<!DOCTYPE html>
<html lang="en">
<head>
<meta charset="utf-8">
<title>Moss &amp; Lark — Book Cover</title>
<link rel="stylesheet" href="https://fonts.googleapis.com/css2?family=Bebas+Neue&family=Oswald:wght@400;500&family=Great+Vibes&display=swap">
<style>
  :root {
    --page-bg: #ffffff;
    --sky-top: #6f7467;
    --sky-mid: #8e9183;
    --cloud: #b3b2a5;
    --storm: #4a5052;
    --storm-deep: #262a2e;
    --type-light: #ffffff;
    --type-soft: #e9e9e6;
  }
  * { margin: 0; padding: 0; box-sizing: border-box; }
  html, body {
    width: 1200px;
    height: 675px;
    overflow: hidden;
    background: var(--page-bg);
  }
  .canvas {
    position: relative;
    width: 1200px;
    height: 675px;
    background: var(--page-bg);
  }
  .book-cover {
    position: absolute;
    left: 281px;
    top: 7px;
    width: 327px;
    height: 490px;
    overflow: hidden;
  }
  .cover-photo {
    position: absolute;
    inset: 0;
    background:
      linear-gradient(180deg,
        var(--sky-top) 0%,
        var(--sky-mid) 22%,
        var(--cloud) 30%,
        var(--cloud) 35%,
        var(--storm) 40%,
        #3a3f43 60%,
        var(--storm-deep) 100%);
  }
  .authors {
    position: absolute;
    left: 29px;
    top: 200px;
    font-family: "Oswald", sans-serif;
    font-weight: 500;
    font-size: 10.5px;
    letter-spacing: 0.4px;
    color: var(--type-light);
    text-transform: uppercase;
    white-space: nowrap;
  }
  .title-strong {
    position: absolute;
    left: 20px;
    top: 214px;
    font-family: "Bebas Neue", sans-serif;
    font-size: 118px;
    line-height: 1;
    letter-spacing: 1px;
    color: var(--type-light);
  }
  .title-amp {
    position: absolute;
    left: 104px;
    top: 290px;
    font-family: "Great Vibes", cursive;
    font-size: 96px;
    line-height: 1;
    color: var(--type-light);
  }
  .title-script {
    position: absolute;
    left: 14px;
    top: 344px;
    font-family: "Great Vibes", cursive;
    font-size: 92px;
    line-height: 1;
    color: var(--type-light);
  }
  .subtitle {
    position: absolute;
    left: 0;
    right: 0;
    top: 456px;
    padding: 0 8px;
    font-family: "Oswald", sans-serif;
    font-weight: 400;
    font-size: 9.2px;
    line-height: 1.45;
    text-align: center;
    text-transform: uppercase;
    color: var(--type-soft);
  }
</style>
</head>
<body>
  <main class="canvas">
    <section class="book-cover">
      <div class="cover-photo" role="img" aria-label="Moody photograph: a grey-green sky with a bunch of coloured balloons above a cloud band, and below it a woman in the rain reaching upward toward the balloons"></div>
      <p class="authors">Marnie Tolliver &amp; Dalia Pratt</p>
      <h1 class="book-title">
        <span class="title-strong">MOSS</span>
        <span class="title-amp">&amp;</span>
        <span class="title-script">Lark</span>
      </h1>
      <p class="subtitle">Twelve empowering true stories of women who found strength<br>and hope in times of darkness and despair.</p>
    </section>
  </main>
</body>
</html>
```